Graphics Design of Physics Book

Hi
Size : 8" x 11.25"
We are education book Publication Company and would like to have book cover for "Physics" it has 4 volumes. All 4 having the same color scheme and design except the volume no.
Blue is my personal favorite but u can use any color. Want to have a band at the bottom of the cover to place our Logo “VORLIN Education” a PDF of the same is attached, or you can place logo anywhere according to ur design.
I need “Physics” as title of the book to be visible prominently.
And volume and volume no. should also be Visible and eye catching I prefer a Graphic to enhance the Volume No.
A background pattern can also be a option (it should be vector form so that color can be change later)
Please do not offer any cut and paste design I need very professional presentation.
Volume and Number can be in metallic 3D (CMYK) effect.
only Professional presentation will get feedback.
I have provided a sample artwork for reference do not follow it but can be a reference what I needed !

Target Market(s)

Students Class 9th to 12th

Industry/Entity Type

Education

Font styles to use
Serif

Colors
3176b5
0555a3
85abd2
cadf82
abd036
9bcb3c

Requirements
Must have
• Eye catching.
• “Physics” as title of the book to be visible prominently.
• volume and volume no. should also be Visible and eye catching
• I prefer a Graphic to enhance the Volume No.
• Icons for
• 1. Questions and answers
• 2. Theory Notes
• 3. Tips & Tricks
• 4. Previous Year's Reference Questions
• 5. Covers Complete Syllabus
Nice to have
• decent seamless background or metallic 3d effect (not to be print in special Ink) design should only be in CMYK.
Should not have
• Physics related Pictures or Icons (Specially E=mc2) or any scientist photograph or I Need pure graphic design

```html
<!DOCTYPE html>
<html lang="en">
<head>
<meta charset="utf-8">
<title>Physics Vol 1 — Book Cover</title>
<link rel="stylesheet" href="https://fonts.googleapis.com/css2?family=Alfa+Slab+One&family=Arimo:wght@400;700&display=swap">
<style>
  :root {
    --navy-deep: #16174f;
    --navy: #262a78;
    --blue-mid: #4c5cae;
    --glow: #d4d8ec;
    --band-blue: #0c56a4;
    --white: #ffffff;
    --icon-line: #1c1f55;
  }
  * { margin: 0; padding: 0; box-sizing: border-box; }
  html, body {
    width: 854px; height: 1200px; overflow: hidden;
    background: var(--navy-deep);
  }
  .cover {
    position: relative;
    width: 854px; height: 1200px;
    overflow: hidden;
    font-family: "Arimo", Arial, sans-serif;
  }
  .cover__pattern {
    position: absolute; inset: 0;
    background:
      radial-gradient(ellipse 46% 40% at 50% 51%, var(--glow) 0%, #9ea7d3 22%, var(--blue-mid) 50%, var(--navy) 78%, var(--navy-deep) 100%);
  }
  .title {
    position: absolute; left: 58px; top: 40px;
    width: 748px; height: 210px;
  }
  .title text {
    font-family: "Alfa Slab One", "Rockwell", serif;
    fill: var(--white);
    font-size: 212px;
  }
  .volume-band {
    position: absolute; left: 498px; top: 238px;
    width: 356px; height: 132px;
    background: var(--band-blue);
    box-shadow: 0 4px 10px rgba(0,0,30,.35);
  }
  .volume-band__label {
    position: absolute; left: 30px; top: 8px;
    font-family: "Arimo", Arial, sans-serif;
    font-size: 104px; line-height: 1;
    letter-spacing: -5px;
    color: var(--white);
  }
  .volume-band__number {
    position: absolute; left: 204px; top: 15px;
    width: 92px; height: 102px;
    background: var(--white);
    color: var(--band-blue);
    font-family: "Arimo", Arial, sans-serif;
    font-weight: 700;
    font-size: 96px; line-height: 102px;
    text-align: center;
  }
  .features {
    position: absolute; left: 48px; top: 1040px;
    display: flex; gap: 0;
    list-style: none;
  }
  .feature {
    width: 104px;
    display: flex; flex-direction: column; align-items: center;
    color: var(--white);
    font-weight: 700; font-size: 10.5px; line-height: 11px;
    text-align: center; text-transform: uppercase;
  }
  .feature svg { width: 64px; height: 64px; margin-bottom: 10px; }
  .brand {
    position: absolute; left: 622px; top: 1050px;
    width: 174px; height: 52px;
    display: flex; align-items: center; gap: 8px;
    color: var(--white);
    font-family: "Arimo", Arial, sans-serif;
    font-weight: 700; font-size: 17px; letter-spacing: 1px;
  }
  .brand__mark { width: 14px; height: 14px; background: var(--white); flex: none; }
</style>
</head>
<body>
<main class="cover">
  <div class="cover__pattern" role="img" aria-label="Vector pattern of small four-point stars arranged in concentric rings, glowing pale at the centre and fading to deep navy at the edges"></div>

  <svg class="title" viewBox="0 0 748 210" aria-label="Physics">
    <text x="0" y="164" textLength="744" lengthAdjust="spacingAndGlyphs">Physics</text>
  </svg>

  <div class="volume-band">
    <span class="volume-band__label">Vol</span>
    <span class="volume-band__number">1</span>
  </div>

  <ul class="features">
    <li class="feature">
      <svg viewBox="0 0 64 64" aria-hidden="true">
        <path d="M4 22a18 16 0 1 1 10 14l-7 6 2-9a16 16 0 0 1-5-11z" fill="#fff"/>
        <text x="15" y="30" font-family="Arimo,sans-serif" font-weight="700" font-size="20" fill="var(--icon-line)">?</text>
        <path d="M28 36a18 16 0 1 1 26 13l4 9-10-6a18 16 0 0 1-20-16z" fill="#fff" stroke="var(--icon-line)" stroke-width="2"/>
        <rect x="38" y="27" width="16" height="16" fill="none" stroke="var(--icon-line)" stroke-width="2.5"/>
        <path d="M41 34l5 5 10-12" fill="none" stroke="var(--icon-line)" stroke-width="3"/>
      </svg>
      Questions &amp;<br>Answers
    </li>
    <li class="feature">
      <svg viewBox="0 0 64 64" aria-hidden="true">
        <rect x="6" y="8" width="44" height="50" fill="#fff" stroke="var(--icon-line)" stroke-width="2"/>
        <path d="M12 20h32M12 28h32M12 36h32M12 44h24" stroke="var(--icon-line)" stroke-width="2.5"/>
        <path d="M56 4l5 5-24 24-7 2 2-7z" fill="#fff" stroke="var(--icon-line)" stroke-width="2"/>
      </svg>
      Theory<br>Notes
    </li>
    <li class="feature">
      <svg viewBox="0 0 64 64" aria-hidden="true">
        <rect x="2" y="2" width="60" height="60" fill="#fff"/>
        <path d="M32 4v10" stroke="var(--icon-line)" stroke-width="2"/>
        <path d="M32 14a13 13 0 0 0-8 23v8h16v-8a13 13 0 0 0-8-23z" fill="none" stroke="var(--icon-line)" stroke-width="2.5"/>
        <path d="M26 50h12M28 55h8" stroke="var(--icon-line)" stroke-width="2.5"/>
      </svg>
      Tips &amp;<br>Tricks
    </li>
    <li class="feature">
      <svg viewBox="0 0 64 64" aria-hidden="true">
        <circle cx="24" cy="22" r="16" fill="none" stroke="#fff" stroke-width="4"/>
        <path d="M24 12v11h8" fill="none" stroke="#fff" stroke-width="3"/>
        <text x="36" y="44" font-family="Arimo,sans-serif" font-weight="700" font-size="16" fill="#fff">?</text>
        <text x="20" y="62" font-family="Arimo,sans-serif" font-weight="700" font-size="20" fill="#fff">??</text>
      </svg>
      Previous Year's<br>Reference<br>Questions
    </li>
    <li class="feature">
      <svg viewBox="0 0 64 64" aria-hidden="true">
        <path d="M10 40a24 24 0 0 1 38-30" fill="none" stroke="#fff" stroke-width="6"/>
        <path d="M54 24a24 24 0 0 1-38 30" fill="none" stroke="#fff" stroke-width="6"/>
        <rect x="20" y="16" width="24" height="30" fill="#fff" stroke="var(--icon-line)" stroke-width="2" transform="rotate(-12 32 31)"/>
        <path d="M25 23h14M25 29h14M25 35h10" stroke="var(--icon-line)" stroke-width="2" transform="rotate(-12 32 31)"/>
      </svg>
      Covers<br>Complete<br>Syllabus
    </li>
  </ul>

  <div class="brand">
    <span class="brand__mark"></span>
    <span class="brand__name">VORLIN EDUCATION</span>
  </div>
</main>
</body>
</html>
```